Wordpress Design for my Consulting Company

We want a WordPress site created for our new business. We have created a mock-up of the content we want on the site at https://marcusdellow.example-sites.com/website-5

We are not attached to any of the pictures and just put stock stuff from wix's editor, which we don't have rights to use outside of wix.

We are NOT looking to just port this site to WordPress, we are looking for some creative ways to display the content in a more professional artistic sense.

I have included several logo files and a text file with the colors and Fonts used in the logo. We are not looking to change the logo or the colors used in the logo.

The Schedule appointment links to a page that embeds a bookingnest.example.com calendar. https://bookingnest.example.com/marcus-dellow/brightvale

The final website domain will be enterprisebrightvale.example

Enterprise brightvale is a consulting company that works directly with the business owners and leaders of small businesses between 50-200 employees. We help companies make sure they have the right technology to meet their strategic goals. We are the anti-"Computer Guy" and we focus on business outcomes NOT cool technology gadgets.

The final design should communicate business growth and success.

Target Market(s)

Business Owners of companies with 50-200 employees

Coding

Coded - Design and coding required

Number of Pages Required

1 page

Font styles to use
Serif
Other font styles liked:
• Trajan Pro Bold, Open Sans

Requirements
Must have
• Should focus on consulting rather than technology.
• Should show the customer as the hero and we are just their guide.
• Must use the logo provided and the colors and fonts in the text file provided. Any other colors and fonts must be complementary.
• The design should scale for all devices computer, iPad, or phone
Should not have
• Should not focus on technology, we are the anti-"Computer Guy" and we focus on business outcomes NOT cool technology gadgets.

```html
<!DOCTYPE html>
<html lang="en">
<head>
<meta charset="utf-8">
<title>Brightvale — Technology advisors that get business</title>
<link href="https://fonts.googleapis.com/css2?family=Playfair+Display:wght@400;700&family=Open+Sans:wght@400;600;700&display=swap" rel="stylesheet">
<style>
:root{
  --ink:#2f3b44;
  --slate:#3d4a53;
  --slate-2:#4a5963;
  --slate-3:#55636c;
  --copper:#c8764a;
  --copper-2:#d0875c;
  --copper-3:#c98050;
  --copper-4:#d49168;
  --mist:#f4f4f6;
  --line:#e3e3e6;
  --muted:#6c7278;
  --white:#ffffff;
  --serif:'Playfair Display', Georgia, serif;
  --sans:'Open Sans', Arial, sans-serif;
}
*{box-sizing:border-box;margin:0;padding:0}
html,body{width:1200px;height:3805px;overflow:hidden}
body{position:relative;font-family:var(--sans);color:var(--ink);background:var(--white)}
.abs{position:absolute}
.btn{position:absolute;background:var(--copper);color:var(--white);border-radius:16px;font:italic 700 12px/30px var(--sans);text-align:center}

/* header */
.site-header{position:absolute;left:0;top:0;width:1200px;height:81px;background:var(--white)}
.brand{position:absolute;left:43px;top:20px;display:flex;align-items:center;gap:12px}
.brand-dot{width:40px;height:40px;border-radius:50%;background:var(--slate)}
.brand-name{font:700 26px/1 var(--serif);color:var(--slate);letter-spacing:1px}
.nav a{position:absolute;top:29px;font:400 14px/1 var(--sans);color:var(--ink);text-decoration:none}
.nav a.active{color:var(--copper)}
.header-btn{left:961px;top:22px;width:199px;height:34px;line-height:34px}

/* hero */
.hero{position:absolute;left:0;top:81px;width:1200px;height:559px;background:linear-gradient(110deg,#8e9ea6 0%,#b9c5ca 40%,#6d8089 75%,#39474f 100%)}
.hero-title{position:absolute;left:160px;top:178px;color:var(--white);font-family:var(--serif)}
.hero-title .l1{font-size:34px;display:block}
.hero-title .l2{font-size:50px;font-weight:700;display:block;margin-top:2px}
.hero-sub{position:absolute;left:160px;top:303px;color:var(--white);font-size:15px}
.hero-btn{left:160px;top:366px;width:198px;height:30px}
.hero-arrow{position:absolute;top:268px;color:var(--white);font-size:26px}

/* benefit tabs */
.tabs{position:absolute;left:0;top:640px;width:1200px;height:160px;display:flex}
.tab{position:relative;width:400px;height:160px;background:var(--slate-3);padding:52px 0 0 40px;color:var(--white)}
.tab:nth-child(2){background:var(--slate-2)}
.tab:nth-child(3){background:var(--slate)}
.tab small{display:block;font:italic 13px/1 var(--serif);color:var(--copper-2)}
.tab b{display:block;margin-top:12px;font:700 15px/1 var(--serif)}
.tab svg{position:absolute;right:34px;top:50px}
.tab.on::after{content:"";position:absolute;left:0;bottom:0;width:400px;height:5px;background:var(--copper)}

/* tired section */
.tired{position:absolute;left:0;top:800px;width:1200px;height:743px;background:var(--mist)}
.sec-title{position:absolute;width:1200px;text-align:center;font:400 33px/38px var(--serif);color:var(--ink)}
.tired-photo{position:absolute;left:0;top:146px;width:601px;height:437px;background:linear-gradient(120deg,#d6dde0,#eef1f2 55%,#c9d0d3)}
.checks{position:absolute;left:560px;top:182px;width:520px}
.check{position:absolute;left:0;display:flex;align-items:flex-start}
.check i{display:block;width:40px;height:40px;border-radius:50%;background:var(--white);box-shadow:0 1px 4px rgba(0,0,0,.08);flex:none;position:relative}
.check i svg{position:absolute;left:12px;top:13px}
.check.on i{background:var(--copper)}
.check p{margin-left:65px;margin-top:9px;font-size:14px;line-height:21px;color:var(--muted);width:390px}
.tired-btn{left:525px;top:649px;width:150px;height:30px}

/* statement band */
.statement{position:absolute;left:0;top:1543px;width:1200px;height:322px;background:linear-gradient(100deg,#56646c,#6f7d85 50%,#4e5b63)}
.statement p{position:absolute;left:160px;top:80px;width:880px;color:var(--white);font:400 30px/40px var(--serif)}

/* testimonial */
.testimonial{position:absolute;left:0;top:1865px;width:1200px;height:512px;background:var(--white)}
.quote-mark{position:absolute;left:0;top:78px;width:1200px;text-align:center;font:700 70px/1 var(--serif);color:var(--copper)}
.quote{position:absolute;left:300px;top:160px;width:600px;text-align:center;font:italic 16px/28px var(--serif);color:var(--muted)}
.avatar{position:absolute;left:560px;top:302px;width:80px;height:80px;border-radius:50%;background:linear-gradient(#bfc5c9,#7e878d)}
.who{position:absolute;left:0;top:396px;width:1200px;text-align:center}
.who b{display:block;font:700 16px/1 var(--serif)}
.who span{display:block;margin-top:6px;font-size:12px;color:var(--muted)}
.t-arrow{position:absolute;top:332px;color:#b9bcbf;font-size:20px}

/* mindset */
.mindset{position:absolute;left:0;top:2377px;width:1200px;height:515px;background:var(--mist)}
.mindset p{position:absolute;left:160px;top:148px;width:380px;font-size:20px;line-height:29px;color:var(--ink)}
.mindset-btn{left:160px;top:333px;width:150px;height:30px}
.mindset-photo{position:absolute;left:601px;top:79px;width:579px;height:360px;background:linear-gradient(100deg,#f1f1f1,#c7c7c7 45%,#3a3a3a 70%,#cfcfcf)}

/* steps */
.steps-title{position:absolute;left:0;top:2960px;width:1200px;text-align:center;font:400 33px/38px var(--serif)}
.steps{position:absolute;left:0;top:3032px;width:1200px;height:281px;display:flex}
.step{position:relative;width:300px;height:281px;padding:90px 30px 0 40px;color:var(--white);background:var(--copper)}
.step:nth-child(2){background:var(--copper-2)}
.step:nth-child(3){background:var(--copper-3)}
.step:nth-child(4){background:var(--copper-4)}
.step h3{font:700 16px/1 var(--serif)}
.step p{margin-top:14px;font-size:12px;line-height:19px;width:220px}
.step svg{position:absolute;right:36px;top:44px}

/* contact */
.contact{position:absolute;left:0;top:3313px;width:1200px;height:492px;background:var(--slate);color:var(--white)}
.contact h2{position:absolute;left:160px;top:78px;font:400 34px/1 var(--serif)}
.call{position:absolute;left:160px;top:135px;font-size:20px}
.mail{position:absolute;left:160px;top:165px;font-size:12px}
.addr{position:absolute;left:160px;top:202px;font-size:12px;line-height:18px}
.social{position:absolute;left:160px;top:330px;display:flex;gap:14px}
.social i{display:block;width:32px;height:32px;border-radius:50%;border:1px solid rgba(255,255,255,.5)}
.social i.on{background:var(--copper);border-color:var(--copper)}
.field{position:absolute;background:var(--white);border-radius:2px;font-size:11px;color:#9aa0a5;padding:9px 12px}
.send{left:462px;top:333px;width:100px;height:30px}
.rule{position:absolute;top:427px;height:1px;background:rgba(255,255,255,.35)}
.copy{position:absolute;left:0;top:420px;width:1200px;text-align:center;font-size:12px;color:#c6ccd0}
.up{position:absolute;left:1083px;top:411px;width:32px;height:32px;border-radius:50%;background:var(--copper)}
.up svg{position:absolute;left:10px;top:10px}
</style>
</head>
<body>

<header class="site-header">
  <div class="brand"><span class="brand-dot"></span><span class="brand-name">BRIGHTVALE</span></div>
  <nav class="nav">
    <a class="active" style="left:652px">Home</a>
    <a style="left:721px">About</a>
    <a style="left:790px">Why Us?</a>
    <a style="left:873px">Contact</a>
  </nav>
  <span class="btn header-btn">Schedule Appointment</span>
</header>

<section class="hero">
  <div class="abs" role="img" aria-label="Photo of two businessmen reviewing documents at a desk" style="inset:0"></div>
  <h1 class="hero-title"><span class="l1">Technology advisors that</span><span class="l2">"Get" business.</span></h1>
  <p class="hero-sub">We help you leverage technology <em>to create</em> a competitive advantage.</p>
  <span class="btn hero-btn">Schedule Appointment</span>
  <span class="hero-arrow" style="left:88px">‹</span>
  <span class="hero-arrow" style="left:1088px">›</span>
</section>

<div class="tabs">
  <div class="tab on"><small>We get ...</small><b>Reducing time to decision</b>
    <svg width="30" height="30" viewBox="0 0 30 30" fill="none" stroke="#fff" stroke-width="2"><path d="M8 26 L14 14 L10 12 L22 4 L16 16 L20 18 Z"/></svg></div>
  <div class="tab"><small>We get ...</small><b>Leverage your business</b>
    <svg width="32" height="30" viewBox="0 0 32 30" fill="none" stroke="#c8764a" stroke-width="2"><path d="M16 4v22M8 26h16M4 8h24M4 8l-3 9h8zM28 8l-3 9h8z"/></svg></div>
  <div class="tab"><small>We get ...</small><b>Standardized customer experience</b>
    <svg width="36" height="30" viewBox="0 0 36 30" fill="none" stroke="#c8764a" stroke-width="2"><circle cx="12" cy="10" r="5"/><circle cx="25" cy="10" r="5"/><path d="M3 26c0-6 4-9 9-9s9 3 9 9M16 26c0-6 4-9 9-9s9 3 9 9"/></svg></div>
</div>

<section class="tired">
  <h2 class="sec-title" style="top:75px">Are you tired of<br>"Computer Guys" that...</h2>
  <div class="tired-photo" role="img" aria-label="Photo of a stressed businessman at a laptop"></div>
  <div class="checks">
    <div class="check" style="top:0"><i><svg width="16" height="14" viewBox="0 0 16 14" fill="none" stroke="#c8764a" stroke-width="2"><path d="M2 7l4 4 8-9"/></svg></i><p>Don't want to be involved in business strategy.</p></div>
    <div class="check on" style="top:50px"><i><svg width="16" height="14" viewBox="0 0 16 14" fill="none" stroke="#fff" stroke-width="2"><path d="M2 7l4 4 8-9"/></svg></i><p>Say "No!" but do not give options on how to achieve your business outcome.</p></div>
    <div class="check" style="top:118px"><i><svg width="16" height="14" viewBox="0 0 16 14" fill="none" stroke="#c8764a" stroke-width="2"><path d="M2 7l4 4 8-9"/></svg></i><p>Can't explain how a technology will create business value, but insist it is necessary.</p></div>
    <div class="check" style="top:186px"><i><svg width="16" height="14" viewBox="0 0 16 14" fill="none" stroke="#c8764a" stroke-width="2"><path d="M2 7l4 4 8-9"/></svg></i><p>Give you the excuse, "You never asked."</p></div>
    <div class="check" style="top:244px"><i><svg width="16" height="14" viewBox="0 0 16 14" fill="none" stroke="#c8764a" stroke-width="2"><path d="M2 7l4 4 8-9"/></svg></i><p>Recommend technology when a simple process or policy change would have the same effect.</p></div>
    <div class="check" style="top:314px"><i><svg width="16" height="14" viewBox="0 0 16 14" fill="none" stroke="#c8764a" stroke-width="2"><path d="M2 7l4 4 8-9"/></svg></i><p>Suggest expensive solutions that are just thrown away, soon after they are deployed.</p></div>
  </div>
  <span class="btn tired-btn">Contact Us Today!</span>
</section>

<section class="statement" role="img" aria-label="Muted photo of a business meeting behind the text">
  <p>We get the frustration of working with consultants and experts who don't listen or take the time to understand your company goals and vision. We believe technology should serve your business, not the other way around.</p>
</section>

<section class="testimonial">
  <div class="quote-mark">“</div>
  <p class="quote">I knew I was behind, I just didn't know by how much. We had years of hand-aided solutions and Brightvale helped us stabilize our environment and position ourselves to compete in the quickly changing world of copy and print ...</p>
  <span class="t-arrow" style="left:497px">‹</span>
  <div class="avatar" role="img" aria-label="Portrait of the client"></div>
  <span class="t-arrow" style="left:695px">›</span>
  <div class="who"><b>Dana Whitcomb</b><span>Print Harbor</span></div>
</section>

<section class="mindset">
  <p>Computer guys frustrate business leaders because they don't have a business mindset. Brightvale advises on strategy that helps companies apply technology to gain a competitive advantage.</p>
  <span class="btn mindset-btn">Contact Us Today!</span>
  <div class="mindset-photo" role="img" aria-label="Photo of a hand moving a chess piece"></div>
</section>

<h2 class="steps-title">The Four Steps to Aligning<br>Technology to your Business Strategy!</h2>
<div class="steps">
  <div class="step"><h3>Discover</h3><p>Identify what is going on behind the scenes, and create a snapshot of the current infrastructure.</p>
    <svg width="30" height="30" viewBox="0 0 30 30" fill="none" stroke="#fff" stroke-width="2"><circle cx="18" cy="12" r="8"/><path d="M12 18L3 27"/></svg></div>
  <div class="step"><h3>Prioritize</h3><p>Meet to decide which solutions and policies will have the greatest impact on reaching the companies goals.</p>
    <svg width="30" height="30" viewBox="0 0 30 30" fill="none" stroke="#fff" stroke-width="2"><path d="M3 13h5v14H3zM8 14l6-10c3 0 3 3 2 7h8c2 0 3 2 2 4l-3 10H8"/></svg></div>
  <div class="step"><h3>Implement</h3><p>Implement those things that will give the greatest return on investment.</p>
    <svg width="30" height="30" viewBox="0 0 30 30" fill="none" stroke="#fff" stroke-width="2"><circle cx="19" cy="10" r="6"/><circle cx="9" cy="21" r="5"/><path d="M13 17l2-3"/></svg></div>
  <div class="step"><h3>Maintain</h3><p>Create a system that keeps your technology aligned as strategy adjusts over time.</p>
    <svg width="30" height="30" viewBox="0 0 30 30" fill="none" stroke="#fff" stroke-width="2"><path d="M4 26l12-12M16 14a6 6 0 1 0 4-10l-3 4 3 3 4-3a6 6 0 0 1-8 6"/></svg></div>
</div>

<footer class="contact">
  <h2>Contact Us</h2>
  <p class="call">Call Us: (555) 014-2290</p>
  <p class="mail">mdellow@enterprisebrightvale.example</p>
  <p class="addr">Address:<br>1840 Linden Park Road,<br>Suite 310 Maple Crossing,<br>TX 75001</p>
  <div class="social"><i></i><i class="on"></i><i></i></div>
  <div class="field" style="left:462px;top:140px;width:294px;height:30px">Name</div>
  <div class="field" style="left:760px;top:140px;width:280px;height:30px">Email</div>
  <div class="field" style="left:462px;top:188px;width:294px;height:30px">Phone</div>
  <div class="field" style="left:760px;top:188px;width:280px;height:30px">Subject</div>
  <div class="field" style="left:462px;top:236px;width:578px;height:79px">Type Your Message</div>
  <span class="btn send">Send</span>
  <div class="rule" style="left:160px;width:340px"></div>
  <div class="rule" style="left:700px;width:380px"></div>
  <p class="copy">©2018 by Enterprise Brightvale</p>
  <div class="up"><svg width="12" height="12" viewBox="0 0 12 12" fill="none" stroke="#fff" stroke-width="2"><path d="M2 8l4-4 4 4"/></svg></div>
</footer>

</body>
</html>
```